BrewHaunt coffee packaging design

We need a vector design (AI) for the printing of our coffee bags.

The bags are double sided. Front will be simple with logo and web address. Back will have lots of information (below) and the wording can be changed to suit if required.

Actual bag dimensions are: 240mm wide x 335mm high (each side) artwork should be inside those sizes.

Front:
Requires - BrewHaunt cup logo, web address (brewhaunt.com.au) in lowercase Papyrus font and the words BREW HAUNT in uppercase.
**added** The front will also need a 90mm x 35mm no artwork area so we can place a sticker.

Back:
1.
Velvet Kettle Logo (needs to be entire unmodified logo) and the tagline of "Overall winner of Australia's biggest coffee roasting competition"

2.
BrewHaunt is a family business, proudly Australian owned and operated. We strive to provide amazing coffee, excellent service and great value to all our customers.

3.
Our coffee is fresh roasted to order and shipped same day.

4.
50c from every kilogram sold goes directly to projects in coffee growing regions. TrueLoop is the Fairest Trade of all - see: trueloop.net

Logos are attached and higher resolution ones are available if needed.

Requirements
Must have
• Per the description, BrewHaunt logo and webaddress on the front and Velvet Kettle logo on the back are required.

```html
<!DOCTYPE html>
<html lang="en">
<head>
<meta charset="utf-8">
<title>BrewHaunt coffee bag – front and back</title>
<link rel="stylesheet" href="https://fonts.googleapis.com/css2?family=Aladin&family=Questrial&display=swap">
<style>
  :root {
    --paper: #ffffff;
    --orange: #f07d10;
    --orange-deep: #f26a0a;
    --yellow: #f7d21a;
    --yellow-pale: #f5ea1e;
    --brown-light: #8c6a3e;
    --brown: #4a2c16;
    --brown-dark: #2a170b;
    --stitch: #d98a3a;
    --ink: #1a1a1a;
    --web-ink: #5a3410;
    --display: "Aladin", fantasy;
    --sans: "Questrial", sans-serif;
  }
  * { margin: 0; padding: 0; box-sizing: border-box; }
  html, body { width: 1200px; height: 900px; overflow: hidden; background: var(--paper); }
  .sheet { position: relative; width: 1200px; height: 900px; }
  .bag-side { position: absolute; display: block; }
  .bag-front { left: 113px; top: 192px; width: 410px; height: 563px; }
  .bag-back { left: 655px; top: 195px; width: 408px; height: 562px; }
  .side-label {
    position: absolute; font-family: var(--sans); font-size: 46px;
    color: var(--ink); font-weight: 400;
  }
  .label-front { left: 410px; top: 778px; }
  .label-back { left: 952px; top: 788px; }
  .display { font-family: var(--display); }
  .sans { font-family: var(--sans); }
</style>
</head>
<body>
<main class="sheet">

  <svg class="bag-side bag-front" viewBox="0 0 410 563" aria-label="Bag front">
    <defs>
      <linearGradient id="front-sky" x1="0" y1="0" x2="1" y2="1">
        <stop offset="0" stop-color="#f5a01a"/>
        <stop offset="0.5" stop-color="#f7c41c"/>
        <stop offset="1" stop-color="#f9e71a"/>
      </linearGradient>
      <linearGradient id="front-ground" x1="0" y1="0" x2="0" y2="1">
        <stop offset="0" stop-color="#f8a814"/>
        <stop offset="1" stop-color="#f5ea1e"/>
      </linearGradient>
      <linearGradient id="front-band" x1="0" y1="0" x2="0" y2="1">
        <stop offset="0" stop-color="#8c6a3e"/>
        <stop offset="1" stop-color="#3a2210"/>
      </linearGradient>
      <linearGradient id="front-ribbon" x1="0" y1="0" x2="0" y2="1">
        <stop offset="0" stop-color="#8a6236"/>
        <stop offset="0.45" stop-color="#4a2c16"/>
        <stop offset="1" stop-color="#2a170b"/>
      </linearGradient>
    </defs>
    <rect class="sky" width="410" height="253" fill="url(#front-sky)"/>
    <rect class="ground" y="253" width="410" height="310" fill="url(#front-ground)"/>
    <rect class="band" y="253" width="410" height="125" fill="url(#front-band)"/>
    <line x1="0" y1="266" x2="410" y2="266" stroke="var(--stitch)" stroke-dasharray="3 2" stroke-width="0.8"/>
    <line x1="0" y1="366" x2="410" y2="366" stroke="var(--stitch)" stroke-dasharray="3 2" stroke-width="0.8"/>
    <path class="ribbon" d="M109 0 H315 V383 L109 476 Z" fill="url(#front-ribbon)"/>
    <path class="ribbon-stitch" d="M115 0 V463 L309 376 V0" fill="none" stroke="var(--stitch)" stroke-dasharray="3 2" stroke-width="0.8"/>
    <circle class="brand-mark" cx="212" cy="130" r="50" fill="var(--orange)"/>
    <text class="display brand-name" x="212" y="266" text-anchor="middle" font-size="38" fill="var(--orange)" letter-spacing="2">BREW</text>
    <text class="display brand-name" x="212" y="302" text-anchor="middle" font-size="38" fill="var(--orange)" letter-spacing="2">HAUNT</text>
    <text class="sans" x="212" y="330" text-anchor="middle" font-size="9.5" fill="var(--orange)">FAIR TRADE COFFEE</text>
    <text class="sans" x="212" y="356" text-anchor="middle" font-size="10.5" fill="var(--orange)">The finest selection of coffee beans</text>
    <text class="sans" x="212" y="381" text-anchor="middle" font-size="5" fill="var(--orange)">net 30G</text>
    <text class="display web-address" x="212" y="548" text-anchor="middle" font-size="20" fill="var(--web-ink)">brewhaunt.com.au</text>
  </svg>

  <svg class="bag-side bag-back" viewBox="0 0 408 562" aria-label="Bag back">
    <defs>
      <linearGradient id="back-sky" x1="0" y1="0" x2="1" y2="1">
        <stop offset="0" stop-color="#f5a01a"/>
        <stop offset="0.5" stop-color="#f7c41c"/>
        <stop offset="1" stop-color="#f9e71a"/>
      </linearGradient>
      <linearGradient id="back-ground" x1="0" y1="0" x2="0" y2="1">
        <stop offset="0" stop-color="#f8a814"/>
        <stop offset="1" stop-color="#f5ea1e"/>
      </linearGradient>
      <linearGradient id="back-band" x1="0" y1="0" x2="0" y2="1">
        <stop offset="0" stop-color="#8c6a3e"/>
        <stop offset="1" stop-color="#3a2210"/>
      </linearGradient>
      <linearGradient id="back-ribbon" x1="0" y1="0" x2="0" y2="1">
        <stop offset="0" stop-color="#8a6236"/>
        <stop offset="0.45" stop-color="#4a2c16"/>
        <stop offset="1" stop-color="#2a170b"/>
      </linearGradient>
      <linearGradient id="silver" x1="0" y1="0" x2="1" y2="0">
        <stop offset="0" stop-color="#6d6d6d"/>
        <stop offset="0.3" stop-color="#f2f2f2"/>
        <stop offset="0.7" stop-color="#ffffff"/>
        <stop offset="1" stop-color="#6d6d6d"/>
      </linearGradient>
      <linearGradient id="emblem-tone" x1="0" y1="0" x2="0" y2="1">
        <stop offset="0" stop-color="#8f8fd6"/>
        <stop offset="0.5" stop-color="#e89a2a"/>
        <stop offset="1" stop-color="#f4f0ea"/>
      </linearGradient>
    </defs>
    <rect class="sky" width="408" height="250" fill="url(#back-sky)"/>
    <rect class="ground" y="250" width="408" height="312" fill="url(#back-ground)"/>
    <rect class="band" y="250" width="408" height="125" fill="url(#back-band)"/>
    <line x1="0" y1="263" x2="408" y2="263" stroke="var(--stitch)" stroke-dasharray="3 2" stroke-width="0.8"/>
    <line x1="0" y1="363" x2="408" y2="363" stroke="var(--stitch)" stroke-dasharray="3 2" stroke-width="0.8"/>
    <path class="ribbon" d="M107 0 H303 V455 L107 547 Z" fill="url(#back-ribbon)"/>
    <path class="ribbon-stitch" d="M113 0 V534 L297 448 V0" fill="none" stroke="var(--stitch)" stroke-dasharray="3 2" stroke-width="0.8"/>

    <rect class="award-card" x="128" y="0" width="154" height="175" fill="var(--paper)"/>
    <rect x="133" y="0" width="144" height="170" fill="none" stroke="var(--stitch)" stroke-dasharray="2 2" stroke-width="0.6"/>
    <rect class="award-emblem" x="148" y="30" width="114" height="112" rx="10" fill="url(#emblem-tone)" role="img" aria-label="Velvet Kettle award emblem"/>
    <text class="sans award-name" x="205" y="160" text-anchor="middle" font-size="11" fill="var(--orange)">Velvet Kettle</text>

    <text class="sans" x="205" y="199" text-anchor="middle" font-size="10.5" fill="var(--orange)">Overall winner of Australia's</text>
    <text class="sans" x="205" y="214" text-anchor="middle" font-size="10.5" fill="var(--orange)">biggest coffee roasting competition</text>
    <text class="sans" x="205" y="234" text-anchor="middle" font-size="4.6" fill="var(--orange)">BrewHaunt is a family business, proudly Australian owned</text>
    <text class="sans" x="205" y="240" text-anchor="middle" font-size="4.6" fill="var(--orange)">and operated. We strive to provide amazing coffee,</text>
    <text class="sans" x="205" y="253" text-anchor="middle" font-size="4.6" fill="var(--orange)">excellent service and great value to all our customers.</text>
    <text class="sans" x="205" y="275" text-anchor="middle" font-size="8.5" fill="var(--orange)">Our coffee is fresh roasted to</text>
    <text class="sans" x="205" y="288" text-anchor="middle" font-size="8.5" fill="var(--orange)">order and shipped same day.</text>

    <rect class="trade-band" x="105" y="320" width="200" height="72" fill="url(#silver)"/>
    <text class="sans trade-name" x="205" y="336" text-anchor="middle" font-size="10.5" fill="var(--ink)">TrueLoop</text>
    <rect class="trade-emblem" x="181" y="342" width="48" height="32" rx="14" fill="#3f5a4a" role="img" aria-label="TrueLoop fair trade emblem"/>
    <text class="sans" x="205" y="385" text-anchor="middle" font-size="4.6" fill="var(--ink)">"gives a little back"</text>

    <text class="sans" x="205" y="411" text-anchor="middle" font-size="4.8" fill="var(--orange)">50c from every kilogram sold goes</text>
    <text class="sans" x="205" y="419" text-anchor="middle" font-size="4.8" fill="var(--orange)">directly to projects in coffee growing regions.</text>
    <text class="sans" x="205" y="427" text-anchor="middle" font-size="4.8" fill="var(--orange)">TrueLoop is the</text>
    <text class="sans" x="205" y="435" text-anchor="middle" font-size="4.8" fill="var(--orange)">Fairest Trade of all - see: trueloop.net</text>

    <text class="display web-address" x="280" y="539" text-anchor="middle" font-size="20" fill="var(--web-ink)">brewhaunt.com.au</text>
  </svg>

  <p class="side-label label-front">Front</p>
  <p class="side-label label-back">Back</p>
</main>
</body>
</html>
```